Alcohol Marketing website

Home page and information page design, details as follows

CLIENT PURPOSE
Increase online visibility and create good contacts to increase business.

SERVICES
Drinks Marketing Consultancy
Brand Representation
Spirit Brand Sales & Marketing
Brand Development
Brand Distribution
Brand Launch & Introductions

COMPETITION
merrycasks.co.uk -
talvoranbrands.co.uk -

WEBSITE(S) CLIENT LIKES
Small competitors I admire:
http://www.merrycasks.co.uk/main.htm
http://www.talvoranbrands.com
http://www.vaultpicks.co.uk/spiritsliqueursbybrand.php
http://www.quellomarks.com/page1.html
http://www.zirnopaxtra.co.uk/index.asp

Nice page layout:
http://www.kvworks.com/
http://www.dmhallies.com/
http://www.pelvik.com/index.cfm?do=pelvik.home

WEBSITE CLIENT DOES NOT LIKE
http://www.tidemarque.com/
http://www.parlour-labels.com/
http://www.yonderpours.co.uk/aboutUs.html
http://www.graincorkhouse.com/
http://www.orbitmarques.co.uk/default.asp
http://www.summit-labels.co.uk/start.htm
http://www.durlay.co.uk/
http://www.pkcasks.com/default2.aspx
http://www.quaff-marques.co.uk/mainpage.aspx

COMPANY LOGO
Customer has a company logo (Supplied)

COLOURS:
Blue
White

STRAPLINE:
No

WEBSITE THEME: Marketing

IMAGES THAT BEST REFLECT THE COMPANY:
Spirits / Drinks

HEADER IMAGE:
Spirits / Brands

PAGES:
home
strength& flavour
a little about us
our spirit marketing
big brand success
speak to us

USER JOURNEYS:
General Service > Land on website >Navigation > Info Pages > Contact Form
Questions > Land on website > Message Banners > Info Pages > Contact Form
Contact > Land on website > Clear Telephone / Email Banner > Contact Form

CALL TO ACTION BANNER:
If you need help making your drink the next big brand, speak to us today.

KEYWORDS THAT RELATE TO THE BUSINESS:
brand marketing
drinks marketing
spirits marketing
brand marketing strategy
alcoholic drinks marketing
Drinks Brand Development

LOCATION(S):
United Kingdom -
Worldwide -

Target Market(s)

Male & Female
30-60
Marketing Directors
Brand Developers
Export Directors
Brand Managers

Industry/Entity Type

Marketing

Number of Pages Required

2 pages

Requirements
Must have
• This design will be integrated into wordpress, I have attached a wireframe of what we need, this is NOT a strict guide but contains content that is essential, the wireframes shows the priority of statements and products. the images supplied need to sell the products and services.
The main banner will eventually be animated so this needs to be taken into account.
The cliemt has supplied images which will need to be used in the design , however if you feel you have better images in the same style then they can be used.
Nice to have
• animation included, Jquery
Should not have
• NO fully flash sites or designs, this site will be Search engine optimised and updateable

```html
<!DOCTYPE html>
<html lang="en">
<head>
<meta charset="utf-8">
<title>Proof &amp; Palate – Drinks Brand Marketing</title>
<link rel="stylesheet" href="https://fonts.googleapis.com/css2?family=Questrial&family=Montserrat:wght@700&display=swap">
<style>
:root{
  --page-bg:#ffffff;
  --sheet:#ffffff;
  --sheet-edge:#d4d4d4;
  --blue:#11b5e8;
  --blue-deep:#0a9ad0;
  --blue-light:#86daf6;
  --blue-mist:#d3eefa;
  --card-edge:#2aa9dc;
  --ink:#1b1b1b;
  --ink-soft:#4a4a4a;
  --grey:#8c8c8c;
  --grey-dark:#5c5c5c;
  --white:#ffffff;
}
*{margin:0;padding:0;box-sizing:border-box}
html,body{width:1200px;height:775px;overflow:hidden;background:var(--page-bg)}
body{font-family:"Questrial",sans-serif;color:var(--ink);position:relative}
.sheet{position:absolute;left:32px;top:-12px;width:1133px;height:762px;background:var(--sheet);
  border:1px solid var(--sheet-edge);border-radius:0 0 14px 14px;box-shadow:0 2px 6px rgba(0,0,0,.18)}
.social{position:absolute;left:61px;top:51px;font-size:14px;color:var(--ink-soft)}
.brand{position:absolute;left:480px;top:30px;width:224px;text-align:center;
  font-family:"Montserrat",sans-serif;font-weight:700;font-size:17px;letter-spacing:.2px;color:var(--ink)}
.brand-dot{position:absolute;left:577px;top:62px;width:30px;height:30px;border-radius:50%;background:var(--blue)}
.contact{position:absolute;right:73px;top:35px;text-align:right;font-size:13.5px;line-height:23px;color:var(--ink-soft)}
.nav{position:absolute;left:58px;top:94px;width:1075px;height:67px}
.nav svg{position:absolute;left:0;top:0}
.nav a{position:absolute;top:15px;color:var(--white);text-decoration:none;font-size:15.5px;line-height:18px}
.hero{position:absolute;left:58px;top:174px;width:1075px;height:270px;border:1.5px solid var(--blue);
  border-radius:8px;overflow:hidden;background:var(--white)}
.hero-photo{position:absolute;left:0;top:0;width:620px;height:100%;
  background:linear-gradient(90deg,#1d3a78 0%,#3b73a8 35%,#7fb2cf 60%,rgba(255,255,255,0) 100%)}
.quote{position:absolute;left:679px;top:16px;font-size:43px;line-height:60px;color:var(--grey-dark)}
.quote .light{color:#9a9a9a}
.quote .accent{color:var(--blue)}
.quote .mark{color:#b9b9b9;font-size:40px}
.cite{position:absolute;left:912px;top:206px;font-size:19px;line-height:29px;color:var(--grey-dark)}
.features{position:absolute;left:59px;top:456px;width:1073px;height:274px;border-radius:7px;
  background:linear-gradient(180deg,var(--blue-light) 0%,var(--blue) 60%,var(--blue-deep) 100%)}
.card{position:absolute;top:23px;width:330px;height:175px;border:1px solid var(--card-edge);border-radius:11px;
  background:linear-gradient(180deg,#ffffff 0%,#f2fafe 45%,var(--blue-mist) 100%);padding:9px 0 0 24px}
.card h2{font-weight:400;font-size:16.5px;line-height:20px;color:var(--ink);margin-bottom:9px}
.card p{font-size:12.2px;line-height:21px;color:var(--ink)}
.card .more{display:block;margin-top:4px;margin-left:-3px;font-size:14px;color:var(--ink);text-decoration:none}
.keywords{position:absolute;left:0;width:100%;top:223px;text-align:center;font-size:11.8px;line-height:21px;color:var(--ink);font-family:"Montserrat",sans-serif;font-weight:700}
.keywords span{font-family:"Questrial",sans-serif;font-weight:400}
</style>
</head>
<body>
<div class="sheet"></div>

<div class="social">follow chirpline / facepage</div>
<div class="brand">PROOF &amp; PALATE</div>
<div class="brand-dot"></div>
<div class="contact">t: 020 7946 0321<br>e: info@proofandpalate.com</div>

<nav class="nav">
  <svg width="1075" height="67" viewBox="0 0 1075 67" aria-hidden="true">
    <defs>
      <linearGradient id="navFill" x1="0" y1="0" x2="0" y2="1">
        <stop offset="0" stop-color="#16c3f2"/>
        <stop offset="1" stop-color="#0a9acf"/>
      </linearGradient>
    </defs>
    <path d="M8 0 H410 A124 70 0 0 0 658 0 H1067 Q1075 0 1075 8 V59 Q1075 67 1067 67 H8 Q0 67 0 59 V8 Q0 0 8 0 Z" fill="url(#navFill)"/>
  </svg>
  <a href="#" style="left:42px">home<br>page</a>
  <a href="#" style="left:159px">proof<br>&amp; palate</a>
  <a href="#" style="left:289px">a little bit<br>about us</a>
  <a href="#" style="left:685px">our spirit<br>marketing</a>
  <a href="#" style="left:796px">big brand<br>success</a>
  <a href="#" style="left:913px">our<br>blog</a>
  <a href="#" style="left:993px">speak<br>to us</a>
</nav>

<section class="hero">
  <div class="hero-photo" role="img" aria-label="Cocktail glasses lined up along a softly lit bar counter"></div>
  <blockquote class="quote">
    <span class="mark">‘‘</span><span class="light">turning our </span>small<br>
    time whisky <span class="light">into a</span><br>
    <span class="accent">national brand</span><span class="mark">’’</span>
  </blockquote>
  <div class="cite">Dan Hollis<br>Veltra</div>
</section>

<section class="features">
  <article class="card" style="left:15px">
    <h2>22 years experience<br>with big brands</h2>
    <p>Lorem ipsum dolor sit amet, consectetur<br>adipiscing elit. Morbi semper tincidunt enim,<br>in eleifend augue egestas ut. Aliquam ornare<br>ipsum in erat rutrum non venenatis sodales.</p>
    <a class="more" href="#">Read More</a>
  </article>
  <article class="card" style="left:371px">
    <h2>Making your drink<br>the next big brand</h2>
    <p>Lorem ipsum dolor sit amet, consectetur<br>adipiscing elit. Morbi semper tincidunt enim,<br>in eleifend augue egestas ut. Aliquam ornare<br>ipsum in erat rutrum non venenatis sodales.</p>
    <a class="more" href="#">Read More</a>
  </article>
  <article class="card" style="left:727px">
    <h2>350 outlets that<br>listen to what we say</h2>
    <p>Lorem ipsum dolor sit amet, consectetur<br>adipiscing elit. Morbi semper tincidunt enim,<br>in eleifend augue egestas ut. Aliquam ornare<br>ipsum in erat rutrum non venenatis sodales.</p>
    <a class="more" href="#">Read More</a>
  </article>
  <footer class="keywords">
    <span>brand marketing | brand marketing strategy | drinks marketing | spirits marketing | alcoholic drinks marketing | drinks brand development</span><br>
    <span>© 1999-2010 Proof &amp; Palate | terms and conditions | privacy policy</span>
  </footer>
</section>
</body>
</html>
```